Business Card needed for Drainor, a growing Septic Service company

Drainor, a growing local septic service company in Pennsylvania, needs updated business cards. We'd like the business card to feature our logo and communicate that we provide Septic Pumping, Installations/Repairs, Restroom Rentals, and 24/7 Emergency Service. The business card should be eye-catching, bold, and clean/simple. We have been in business almost 10 years and would like to expand and update our business brand and image.

Target Market(s)

Residential and Commercial, New and Current Homeowners

Industry/Entity Type

Service

Contact Information for Business Card

Contact on the business card should be: Dean Harlow Owner & Operator
Phone: 610-555-0187
Email: service@drainor-example.com
Website: www.drainor-example.com
Address: 812 Millbrook Lane Fernvale ST 00000

Font styles to use
Sans Serif

Colors

Designer to choose colors to be used in the design.

Requirements
Must have
• Feature logo on both side of business card.
Nice to have
• We envision the contact information on one side and our services listed on the other side. Utilize the green from the symbol in our logo as part of the design, overall design color scheme should be white, grey, black.

```html
<!DOCTYPE html>
<html lang="en">
<head>
<meta charset="utf-8">
<title>Drainor Business Card</title>
<link rel="stylesheet" href="https://fonts.googleapis.com/css2?family=Montserrat:wght@500&family=Ubuntu:wght@400;500;700&display=swap">
<style>
  :root {
    --brand-green: #86c443;
    --ink: #1e1c1f;
    --paper: #ffffff;
    --backdrop: #86c443;
  }
  * { margin: 0; padding: 0; box-sizing: border-box; }
  html, body {
    width: 1200px;
    height: 1200px;
    overflow: hidden;
    background: var(--backdrop);
    font-family: "Ubuntu", sans-serif;
    color: var(--ink);
  }
  .card {
    position: absolute;
    left: 297px;
    width: 606px;
    height: 347px;
    background: var(--paper);
  }
  .card--front { top: 190px; }
  .card--back { top: 663px; }

  .brand {
    position: absolute;
    display: flex;
    align-items: center;
  }
  .brand__square { background: var(--brand-green); flex: none; }
  .brand__name {
    font-family: "Ubuntu", sans-serif;
    font-weight: 700;
    color: var(--ink);
    line-height: 1;
    letter-spacing: 1px;
  }
  .card--front .brand { left: 168px; top: 85px; gap: 10px; }
  .card--front .brand__square { width: 47px; height: 47px; }
  .card--front .brand__name { font-size: 46px; }

  .services {
    position: absolute;
    left: 0;
    right: 0;
    top: 183px;
    list-style: none;
    text-align: center;
  }
  .services li {
    font-weight: 500;
    font-size: 14.5px;
    letter-spacing: 2.2px;
    line-height: 29.6px;
  }

  .accent-bar {
    position: absolute;
    top: 30px;
    width: 12px;
    height: 99px;
    background: var(--brand-green);
  }
  .accent-bar--left { left: 0; }
  .accent-bar--right { right: 0; }

  .person { position: absolute; left: 48px; top: 50px; }
  .person__name {
    font-weight: 700;
    font-size: 29px;
    letter-spacing: 1px;
    line-height: 1;
  }
  .person__role {
    margin-top: 14px;
    font-family: "Montserrat", sans-serif;
    font-weight: 500;
    font-size: 12.5px;
    letter-spacing: 3.6px;
    color: var(--brand-green);
  }

  .card--back .brand { left: 359px; top: 63px; gap: 6px; }
  .card--back .brand__square { width: 35px; height: 35px; }
  .card--back .brand__name { font-size: 34px; }

  .contacts {
    position: absolute;
    left: 48px;
    top: 215px;
    list-style: none;
  }
  .contacts li {
    display: flex;
    align-items: center;
    height: 28.3px;
    font-size: 11px;
    letter-spacing: 1.1px;
  }
  .contacts svg { width: 22px; height: 22px; margin-right: 6px; flex: none; }
</style>
</head>
<body>

<section class="card card--front">
  <div class="brand">
    <span class="brand__square"></span>
    <span class="brand__name">DRAINOR</span>
  </div>
  <ul class="services">
    <li>Installations/Repairs</li>
    <li>Restroom Rentals</li>
    <li>24/7 Emergency Service</li>
  </ul>
</section>

<section class="card card--back">
  <span class="accent-bar accent-bar--left"></span>
  <span class="accent-bar accent-bar--right"></span>

  <div class="person">
    <h1 class="person__name">Dean Harlow</h1>
    <p class="person__role">Owner &amp; Operator</p>
  </div>

  <div class="brand">
    <span class="brand__square"></span>
    <span class="brand__name">DRAINOR</span>
  </div>

  <ul class="contacts">
    <li>
      <svg viewBox="0 0 22 22" aria-hidden="true">
        <circle cx="11" cy="11" r="10.5" fill="var(--brand-green)"/>
        <path d="M7.5 6.5 l2 -0.5 1 2.5 -1.3 1 a6 6 0 0 0 2.8 2.8 l1 -1.3 2.5 1 -0.5 2 a2 2 0 0 1 -2 1 A9 9 0 0 1 6.5 8.5 a2 2 0 0 1 1 -2 z" fill="#fff"/>
      </svg>
      <span>610-555-0187</span>
    </li>
    <li>
      <svg viewBox="0 0 22 22" aria-hidden="true">
        <circle cx="11" cy="11" r="10.5" fill="var(--brand-green)"/>
        <rect x="6.5" y="7.8" width="9" height="6.5" fill="#fff"/>
        <path d="M6.5 7.8 l4.5 3.5 4.5 -3.5" fill="none" stroke="var(--brand-green)" stroke-width="0.9"/>
      </svg>
      <span>service@drainor-example.com</span>
    </li>
    <li>
      <svg viewBox="0 0 22 22" aria-hidden="true">
        <circle cx="11" cy="11" r="10.5" fill="var(--brand-green)"/>
        <g fill="none" stroke="#fff" stroke-width="0.9">
          <circle cx="11" cy="11" r="4.6"/>
          <ellipse cx="11" cy="11" rx="2" ry="4.6"/>
          <path d="M6.4 11 H15.6 M7.1 8.8 H14.9 M7.1 13.2 H14.9"/>
        </g>
      </svg>
      <span>www.drainor-example.com</span>
    </li>
    <li>
      <svg viewBox="0 0 22 22" aria-hidden="true">
        <circle cx="11" cy="11" r="10.5" fill="var(--brand-green)"/>
        <path d="M11 16.5 C8.5 13.3 7.5 11.8 7.5 10.2 a3.5 3.5 0 0 1 7 0 c0 1.6 -1 3.1 -3.5 6.3 z" fill="#fff"/>
        <circle cx="11" cy="10.2" r="1.3" fill="var(--brand-green)"/>
      </svg>
      <span>812 Millbrook Lane Fernvale ST 00000</span>
    </li>
  </ul>
</section>

</body>
</html>
```